Creative, Innovative PowerPoint Sales Deck Refresh needed

We are a technology firm in the Dallas, TX area and we need the powerpoint presentation used for our sales calls refreshed. This presentation is used in one of the first meetings we have with potential clients, so we want to make a memorable and positive impact - we want something that sets us apart from everyone else. We need 8 master slide templates created for our sales deck and a series of slides within the example sales deck need to be completely refreshed (slides 31-37 and 43 in the sample ppt file) We want a sales deck that is modern, innovative, creative, memorable and whimsical - NOT a typical boring "business" design. Colors should match or compliment the colors used in our logo. The logo in the footer of the attached sample ppt is old - it should be replaced with the newer logo attached. Please take a look at our website to get an idea of our culture and aesthetic www.quorbinlab.com
Updates

Project Deadline Extended
Reason: We have received several designs we like and we want our entire team to have time to give them full consideration before making a decision.

Target Market(s)

Business executives

Industry/Entity Type

Information Technology

Font styles to use
Sans Serif

Requirements
Must have
• Our logo and LedgerWave logo in footer
• Master Slide Templates
• Rework / redesign of slides 31-37 and 43
Nice to have
• We use Raleway font in a lot of our materials

```html
<!DOCTYPE html>
<html lang="en">
<head>
<meta charset="utf-8">
<title>Five Key Areas of User Adoption</title>
<link rel="stylesheet" href="https://fonts.googleapis.com/css2?family=Source+Sans+3:wght@300;400;600;700&display=swap">
<style>
  :root {
    --bg: #ffffff;
    --ink: #1d1d1b;
    --green: #7fc243;
    --ring: #f0f0f0;
    --hero-dark: #2a3550;
    --hero-mid: #8a7f86;
    --hero-light: #d9d4d0;
    --accent-blue: #1c3f6e;
  }
  * { margin: 0; padding: 0; box-sizing: border-box; }
  html, body { width: 1200px; height: 750px; overflow: hidden; background: var(--bg); }
  .slide {
    position: relative;
    width: 1200px;
    height: 750px;
    background: var(--bg);
    font-family: "Source Sans 3", "Helvetica Neue", Arial, sans-serif;
    color: var(--ink);
    overflow: hidden;
  }
  .hero-photo { position: absolute; left: 0; top: 0; }
  .slide-title {
    position: absolute;
    left: 67px;
    top: 50px;
    font-weight: 300;
    font-size: 54px;
    line-height: 64px;
    letter-spacing: -0.3px;
  }
  .cycle { position: absolute; left: 0; top: 0; }
  .area-label {
    font-family: "Source Sans 3", Arial, sans-serif;
    font-weight: 700;
    font-size: 13.5px;
    fill: #ffffff;
    text-anchor: middle;
  }
  .area { fill: var(--green); mix-blend-mode: multiply; }
  .brand-primary {
    position: absolute;
    left: 67px;
    top: 552px;
    display: flex;
    align-items: center;
    gap: 14px;
    font-weight: 400;
    font-size: 22px;
    color: var(--ink);
  }
  .brand-primary .mark {
    width: 44px;
    height: 44px;
    background: var(--accent-blue);
  }
  .brand-partner {
    position: absolute;
    left: 72px;
    top: 650px;
    font-weight: 600;
    font-size: 30px;
    letter-spacing: 1px;
    color: var(--ink);
  }
</style>
</head>
<body>
<main class="slide">
  <svg class="hero-photo" width="1200" height="190" viewBox="0 0 1200 190" role="img" aria-label="Blurred photo of a busy crowd overlaid with a network of white connected technology icons">
    <defs>
      <linearGradient id="heroFill" x1="0" y1="0" x2="1" y2="0.4">
        <stop offset="0" stop-color="var(--hero-dark)"/>
        <stop offset="0.45" stop-color="var(--hero-mid)"/>
        <stop offset="1" stop-color="var(--hero-light)"/>
      </linearGradient>
    </defs>
    <path d="M380 0 H1200 V186 H520 C455 186 420 150 405 90 C396 55 388 25 380 0 Z" fill="url(#heroFill)"/>
  </svg>

  <h1 class="slide-title">Five Key<br>Areas of User<br>Adoption</h1>

  <svg class="cycle" width="1200" height="750" viewBox="0 0 1200 750" aria-hidden="true">
    <g fill="none" stroke="var(--ring)" stroke-width="22">
      <path d="M600 440 A188 188 0 0 1 973 400"/>
      <path d="M972 520 A188 188 0 0 1 598 500"/>
    </g>
    <g fill="var(--ring)">
      <polygon points="530,492 590,420 650,492 624,492 590,454 556,492"/>
      <polygon points="915,445 942,445 975,484 1008,445 1040,445 975,520"/>
    </g>
    <circle class="area" cx="765" cy="397" r="71"/>
    <circle class="area" cx="859" cy="422" r="52"/>
    <circle class="area" cx="693" cy="472" r="45"/>
    <circle class="area" cx="760" cy="533" r="55"/>
    <circle class="area" cx="855" cy="515" r="55"/>
    <text class="area-label" x="760" y="402">Measurement</text>
    <text class="area-label" x="861" y="428">Alignment</text>
    <text class="area-label" x="691" y="477">Alignment</text>
    <text class="area-label" x="760" y="542">Alignment</text>
    <text class="area-label" x="855" y="522">Training</text>
  </svg>

  <div class="brand-primary"><span class="mark"></span><span>quorbinlab</span></div>
  <div class="brand-partner">LEDGERWAVE</div>
</main>
</body>
</html>
```